Tending the Hidden Garden; A Map Toward Calm, Purpose & Belonging

I need a book cover, for the above book title. This is a journey of the heart to know the heart of God. I think on the text, Simple (see below graphic)
Black Lettering for Tending.....Garden
Gold lettering for God
Either gold or black for the subtitle; A Map Toward Calm, Purpose, & Belonging
I would like the below graphic idea only no photograph of a person,
and White background instead of black
Simple Font, like below graphic, but open to suggestions

not age specific, Every person has been given a heart to know God, we are taking the mystery out the process to understand God is Father, loving gracious, ever present, etc. If we know His heart, we realize He's not at a distance, He is there, an ever present help

Security

• Title: Tending the Hidden Garden; A Map Toward Calm, Purpose, & Belonging
• My name, Rob Fenwick
• See Below Graphic

```html
<!DOCTYPE html>
<html lang="en">
<head>
<meta charset="utf-8">
<title>Tending the Hidden Garden — Book Cover</title>
<link href="https://fonts.googleapis.com/css2?family=Bodoni+Moda:wght@400;500&family=Alfa+Slab+One&display=swap" rel="stylesheet">
<style>
  :root {
    --page-bg: #ecebe8;
    --cover-edge: #c3b48e;
    --cover-mid: #e6dcc4;
    --cover-light: #ffffff;
    --ink: #161616;
    --gold-dark: #8c7a4e;
    --gold-mid: #c9b682;
    --gold-light: #f3ecd8;
    --rule: #222222;
  }
  html, body {
    margin: 0;
    padding: 0;
    width: 1200px;
    height: 854px;
    overflow: hidden;
    background: var(--page-bg);
  }
  .stage {
    position: relative;
    width: 1200px;
    height: 854px;
  }
  .cover {
    position: absolute;
    left: 340px;
    top: 37px;
    width: 520px;
    height: 780px;
    background:
      radial-gradient(ellipse 95% 62% at 50% 48%, var(--cover-light) 0%, var(--cover-light) 50%, var(--cover-mid) 78%, var(--cover-edge) 100%);
    box-shadow: 0 10px 18px rgba(0,0,0,0.28);
    font-family: "Bodoni Moda", "Didot", serif;
    color: var(--ink);
    text-align: center;
  }
  .title-top,
  .title-bottom,
  .subtitle,
  .author {
    position: absolute;
    left: 0;
    width: 100%;
    margin: 0;
    font-weight: 400;
  }
  .title-top {
    top: 150px;
    font-size: 58px;
    line-height: 1;
    letter-spacing: -0.5px;
  }
  .rule {
    position: absolute;
    left: 110px;
    width: 300px;
    height: 2px;
    background: var(--rule);
  }
  .rule-upper { top: 215px; }
  .rule-lower { top: 328px; }
  .title-key {
    position: absolute;
    top: 225px;
    left: 0;
    width: 100%;
    margin: 0;
    font-family: "Alfa Slab One", "Rockwell", serif;
    font-weight: 400;
    font-size: 82px;
    line-height: 1;
    letter-spacing: 1px;
    background: linear-gradient(180deg, var(--gold-dark) 0%, var(--gold-mid) 30%, var(--gold-light) 50%, var(--gold-mid) 68%, var(--gold-dark) 100%);
    -webkit-background-clip: text;
    background-clip: text;
    color: transparent;
  }
  .title-bottom {
    top: 334px;
    font-size: 44px;
    line-height: 1;
  }
  .subtitle {
    top: 393px;
    font-size: 23px;
    line-height: 33px;
  }
  .author {
    top: 662px;
    font-size: 34px;
    line-height: 1;
  }
</style>
</head>
<body>
  <main class="stage">
    <section class="cover" aria-label="Book cover">
      <h1 class="book-title">
        <span class="title-top">TENDING THE</span>
        <span class="rule rule-upper"></span>
        <span class="title-key">HIDDEN</span>
        <span class="rule rule-lower"></span>
        <span class="title-bottom">GARDEN</span>
      </h1>
      <p class="subtitle">A Map Toward<br>Calm, Purpose<br>&amp; Belonging</p>
      <p class="author">Rob Fenwick</p>
    </section>
  </main>
</body>
</html>
```